Relaunch / Responsives, modernes Webdesign für ein Campingportal
Zielgruppe
Die zeltwiese GmbH betreibt mit der Plattform www.zeltwiese-online.de eines der führenden Campingportale in Deutschland.
Im Zuge des Relaunches soll ein frisches, neues und modernes Design der Webseite erfolgen und auch die mobile Nutzbarkeit durch ein responsives Design verbessert werden.
Zielgruppe sind Camperinnen und Camper bzw. solche, die es vielleicht einmal werden wollen. Ebenso natürlich auch die Betreiber der Campingplätze, die Mitglied bei zeltwiese sein können und damit bei der Suche, auf der Karte und in den Regionen gefunden werden. Sie sind dann mit einer eigenen Campingplatzseite vertreten, auf der neben allen wichtigen Informationen auch Bilder und Videos vom Platz zu sehen sind.
Aktuell ist im Fokus ein Campingführer (Campingplatzsuche), der wie beschrieben auch per Karte erfolgt und mit Filtern eingeschränkt werden kann. Auch ein Blog ist vorhanden, es wird noch ein Forum geben usw.
Später wird auch noch ein Shop, etc. hinzukommen...
Aufgabenstellung
Das Design soll frisch, modern und natürlich responsiv sein. Das Logo ist dabei weiterhin gesetzt. Daran können Sie also z.B. die Farbgebung übernehmen (v.a. das Grün).
Das Design soll sich nicht mehr rein vertikal ausrichten (wie bisher) sondern horizontal über den gesamten Bildschirm.
Dabei muss z.B. auf der Startseite u.a. auch ein Feld vorhanden sein, in dem man Länder, Regionen oder direkt Campingplätze suchen kann uns sich ein Auswahlfeld mit den vorgeschlagenen Ergebnissen öffnet. So wie bei Hotelportalen zumeist auch.
Es gibt aktuell nachfolgende Seitentypen:
1. Startseite (bisher http://www.zeltwiese-online.de/)
Hier soll u.a. auch ein Feld zur Eingabe eines Landes, einer Region oder eines Platzes existieren, bei dem bei Eingabe Auswahlmöglichkeiten sichtbar werden (wie bei Reiseportalen).
So z.B. bei:
Urlaubsquartiere[Punkt]de
Logis Sofort
Reisepruefer
Auch eine Karte von Europa wäre hier ggf. interessant, die man dann beim Anklicken auf Deutschland fokussiert, danach dann weiter auf die Nordsee usw.
Zudem Flächen wo man besondere Themen oder Regionen noch einmal extra anführt "Campingplätze am Meer", "Campingplätze in den Bergen", "Campingplätze Stadtnah, usw.
Hier zum Beispiel dann auch später eine Grafik zum Shop usw.
Auch kann es einige Flächen geben, die man an Campingplätze vermieten kann, um auf der Startseite präsent zu sein. Also quasi einige exklusive Campingplätze.
Zudem sollte man einen Block haben, wo man besonders nachgefragte Regionenlinks vorstellen kann (Beliebte Reiseziele, Nordseeküste, Alpen, etc.).
Dies müssen aber keine Bilder sein, sondern können auch nur Links sein als Gruppe in einem Block.
Zudem muss es unten ein Textfeld geben, da es sonst schwer wird mit der Regionenseite bei Suchlux weiterhin gut zu ranken.
Selbstverständlich müssen auch Werbeflächen eingeplant sein für Suchlux adse..

```html
<!DOCTYPE html>
<html lang="de">
<head>
<meta charset="utf-8">
<title>zeltwiese – Unterwegs zu Hause</title>
<link rel="stylesheet" href="https://fonts.googleapis.com/css2?family=Raleway:wght@300;400;500;600;700&display=swap">
<style>
:root{
  --navy:#16285f;
  --green:#8cbf1c;
  --text:#555b66;
  --light:#f2f2f2;
  --white:#ffffff;
}
*{box-sizing:border-box;margin:0;padding:0}
html,body{width:1200px;height:2690px;overflow:hidden;background:var(--white);font-family:"Raleway",Arial,sans-serif;color:var(--text)}
.page{position:relative;width:1200px;height:2690px}
.wrap{position:absolute;left:124px;width:950px}

/* header */
.site-header{position:absolute;top:0;left:0;width:1200px;height:93px}
.brand{position:absolute;left:134px;top:30px;display:flex;align-items:center;gap:10px}
.brand-mark{width:26px;height:26px;background:var(--green)}
.brand-name{font-weight:700;font-size:24px;color:var(--navy)}
.main-nav{position:absolute;right:128px;top:27px;display:flex;align-items:center;gap:26px}
.main-nav a{font-size:14px;font-weight:600;color:var(--navy);text-decoration:none}
.main-nav .btn-login{background:var(--navy);color:var(--white);width:136px;height:38px;display:flex;align-items:center;justify-content:center;border-radius:2px}

/* hero */
.hero{position:absolute;top:93px;left:0;width:1200px;height:524px;
  background:linear-gradient(100deg,#a89f88 0%,#8d8a70 25%,#b8a96a 50%,#7e8f45 75%,#a3b274 100%)}
.hero-title{position:absolute;left:124px;top:122px;font-size:67px;line-height:76px;font-weight:700;color:var(--white);letter-spacing:1px}
.search-band{position:absolute;left:0;top:404px;width:1200px;height:120px;background:rgba(235,235,225,.55)}
.search-field{position:absolute;top:24px;width:219px}
.search-field label{display:block;font-size:14px;font-weight:500;color:var(--navy);margin-bottom:8px}
.select{height:38px;background:var(--white);border-radius:2px;font-size:14px;color:#8a8f96;padding:0 12px;display:flex;align-items:center;justify-content:space-between}
.select svg{width:8px;height:14px}
.btn-find{position:absolute;left:854px;top:49px;width:219px;height:38px;background:var(--green);color:var(--white);font-size:14px;font-weight:600;display:flex;align-items:center;justify-content:center;border-radius:2px}

/* ad banner */
.ad-banner{top:657px;height:176px;background:linear-gradient(90deg,#1a4f8e 0%,#2b79b9 50%,#8fd0ea 80%,#b7e3f2 100%);overflow:hidden}
.ad-banner .ad-line1{position:absolute;left:36px;top:20px;font-size:24px;color:var(--white);font-weight:400}
.ad-banner .ad-line2{position:absolute;left:36px;top:42px;font-size:37px;color:var(--white);font-weight:700}
.ad-banner .ad-rule{position:absolute;left:36px;top:90px;width:420px;border-top:1px dashed rgba(255,255,255,.7)}
.ad-banner .ad-line3{position:absolute;left:36px;top:97px;font-size:18px;color:var(--white)}
.ad-badge{position:absolute;top:139px;width:84px;height:26px;background:#111;border-radius:3px;border:1px solid #777}
.ad-phone{position:absolute;left:580px;top:0;width:300px;height:176px;background:linear-gradient(160deg,#d8eef7,#9fc9dc)}

/* themes */
.themes{position:absolute;top:874px;left:0;width:1200px;height:469px;background:var(--navy);color:var(--white);text-align:center}
.section-title{font-size:35px;font-weight:400;letter-spacing:.3px}
.themes .section-title{margin-top:42px}
.section-lead{font-size:13.5px;line-height:20px;margin-top:4px}
.theme{position:absolute;top:172px;width:300px;text-align:center}
.theme svg{height:118px}
.theme h3{font-size:15px;font-weight:700;margin-top:30px}
.theme p{font-size:20px;font-weight:300;margin-top:10px}
.btn-more{display:inline-flex;width:180px;height:38px;background:var(--green);color:var(--white);font-size:14px;font-weight:600;align-items:center;justify-content:center;margin-top:24px}

/* destinations */
.destinations .section-title{position:absolute;top:1408px;left:0;width:1200px;text-align:center;color:var(--green);font-size:34px}
.destinations .section-lead{position:absolute;top:1454px;left:0;width:1200px;text-align:center}
.dest-card{position:absolute;width:219px;height:228px;overflow:hidden;color:var(--white)}
.dest-card .shade{position:absolute;inset:0;background:linear-gradient(180deg,rgba(0,0,0,0) 45%,rgba(0,0,0,.75) 100%)}
.dest-card .country{position:absolute;left:14px;top:160px;font-size:15px;font-weight:700}
.dest-card .region{position:absolute;left:14px;top:185px;font-size:21px;font-weight:300;white-space:nowrap}

/* why */
.why{position:absolute;top:2070px;left:0;width:1200px;height:402px;background:var(--light)}
.why .section-title{text-align:center;color:var(--green);margin-top:42px;font-size:34px}
.why-col{position:absolute;top:114px;width:385px;font-size:13.3px;line-height:20px}
.why-col h3{font-size:14px;font-weight:700;color:var(--navy)}

/* footer */
.site-footer{position:absolute;top:2518px;left:124px;width:950px;font-size:13.5px}
.site-footer h4{margin-top:28px;font-size:15px;font-weight:700;color:var(--navy)}
.country-links{margin-top:12px;line-height:31px}
</style>
</head>
<body>
<div class="page">

<header class="site-header">
  <div class="brand"><span class="brand-mark"></span><span class="brand-name">zeltwiese</span></div>
  <nav class="main-nav">
    <a href="#">Campingplätze</a>
    <a href="#">Campingblog</a>
    <a href="#">Was ist Zeltwiese?</a>
    <a href="#" class="btn-login">Einloggen</a>
  </nav>
</header>

<section class="hero" role="img" aria-label="Foto: Wohnwagen auf einer sonnigen Wiese, Familie beim Frühstück und spielende Kinder">
  <h1 class="hero-title">UNTERWEGS<br>ZU HAUSE</h1>
  <form class="search-band">
    <div class="search-field" style="left:124px"><label>Land</label><div class="select">Deutschland<svg viewBox="0 0 8 14"><path d="M4 0 8 5H0zM4 14 0 9h8z" fill="#555"/></svg></div></div>
    <div class="search-field" style="left:366px"><label>Bundesland</label><div class="select">Baden-Württemberg<svg viewBox="0 0 8 14"><path d="M4 0 8 5H0zM4 14 0 9h8z" fill="#555"/></svg></div></div>
    <div class="search-field" style="left:610px"><label>Region</label><div class="select">Allgäu<svg viewBox="0 0 8 14"><path d="M4 0 8 5H0zM4 14 0 9h8z" fill="#555"/></svg></div></div>
    <div class="btn-find">Campingplätze finden</div>
  </form>
</section>

<aside class="wrap ad-banner">
  <div class="ad-line1">WE'VE ALWAYS BEEN LOCAL</div>
  <div class="ad-line2">NOW WE'RE MOBILE</div>
  <div class="ad-rule"></div>
  <div class="ad-line3">Introducing the LVB Mobile App for PhonePro and Robodroid.</div>
  <div class="ad-badge" style="left:38px"></div>
  <div class="ad-badge" style="left:137px"></div>
  <div class="ad-phone" role="img" aria-label="Foto: Hand hält ein Smartphone mit geöffneter App"></div>
</aside>

<section class="themes">
  <h2 class="section-title">ENTDECKE CAMPING WIE NOCH NIE</h2>
  <p class="section-lead">Lorem ipsum dolor sit amet, consetetur elitr, sed diam nonumy eirmod tempor invidunt<br>ut labore et dolore magna aliquyam erat,</p>

  <div class="theme" style="left:112px">
    <svg viewBox="0 0 120 118" fill="#fff"><path d="M10 50a46 40 0 0 1 72-28L10 50z"/><rect x="40" y="30" width="5" height="60" transform="rotate(-20 42 60)"/><path d="M15 80h80l15-22 6 4-14 22v16h-6V86H70v14h-6V86H30v14h-6V86h-9z"/></svg>
    <h3>Campingplätze am Meer</h3><p>Blicke hinaus auf den Horizont</p><span class="btn-more">Mehr erfahren</span>
  </div>
  <div class="theme" style="left:466px">
    <svg viewBox="0 0 160 118" fill="#fff"><path d="M5 118 65 30l28 40 18 48z"/><path d="M88 5l12 6-12 5zM118 18l10 5-10 4z"/><circle cx="120" cy="62" r="18"/><circle cx="140" cy="70" r="14"/><rect x="104" y="68" width="48" height="16" rx="8"/></svg>
    <h3>Campingplätze in den Bergen</h3><p>Ruhe und frische Luft</p><span class="btn-more">Mehr erfahren</span>
  </div>
  <div class="theme" style="left:785px">
    <svg viewBox="0 0 90 118" fill="#fff"><path d="M0 10h55v108H0z"/><path d="M40 50h50v68H40z"/><g fill="#16285f"><rect x="8" y="18" width="10" height="10"/><rect x="24" y="18" width="10" height="10"/><rect x="8" y="36" width="10" height="10"/><rect x="24" y="36" width="10" height="10"/><rect x="8" y="54" width="10" height="10"/><rect x="8" y="72" width="10" height="10"/><rect x="8" y="90" width="10" height="14"/><rect x="48" y="58" width="9" height="9"/><rect x="62" y="58" width="9" height="9"/><rect x="76" y="58" width="9" height="9"/><rect x="48" y="74" width="9" height="9"/><rect x="62" y="74" width="9" height="9"/><rect x="76" y="74" width="9" height="9"/><rect x="48" y="90" width="9" height="9"/><rect x="62" y="90" width="9" height="9"/><rect x="76" y="90" width="9" height="9"/></g></svg>
    <h3>Campingplätze in der Stadt</h3><p>Am Puls des Lebens</p><span class="btn-more">Mehr erfahren</span>
  </div>
</section>

<section class="destinations">
  <h2 class="section-title">DIE BELIEBTESTEN REISEZIELE FÜR CAMPER</h2>
  <p class="section-lead">Lorem ipsum dolor sit amet, consetetur elitr, sed diam nonumy eirmod tempor invidunt<br>ut labore et dolore magna aliquyam erat,</p>

  <a class="dest-card" style="left:124px;top:1523px;background:linear-gradient(180deg,#9aa0a3,#5c6566 55%,#2f3838)" role="img" aria-label="Foto: Segelboot auf einem See unter grauem Himmel"><span class="shade"></span><span class="country">Deutschland</span><span class="region">Mecklenb. Seenplatte</span></a>
  <a class="dest-card" style="left:367px;top:1523px;background:linear-gradient(160deg,#c9a27a,#7e7560 45%,#3d4a4c)" role="img" aria-label="Foto: bunte Häuser an einer Felsküste"><span class="shade"></span><span class="country">Italien</span><span class="region">Ligurien</span></a>
  <a class="dest-card" style="left:610px;top:1523px;background:linear-gradient(180deg,#f0a77f,#c98f63 45%,#4a3a2a)" role="img" aria-label="Foto: Windmühlen im Abendlicht"><span class="shade"></span><span class="country">Niederlande</span><span class="region">Zeeland</span></a>
  <a class="dest-card" style="left:853px;top:1523px;background:linear-gradient(180deg,#3f6fb3,#7a8d7a 35%,#2e3f55)" role="img" aria-label="Foto: Küstenort am Meer mit Boot"><span class="shade"></span><span class="country">Kroatien</span><span class="region">Istrien</span></a>

  <a class="dest-card" style="left:124px;top:1775px;background:linear-gradient(180deg,#dfe3e5,#5e6d52 45%,#283228)" role="img" aria-label="Foto: Bergsee mit Wald und schneebedecktem Gipfel"><span class="shade"></span><span class="country">Österreich</span><span class="region">Kärnten</span></a>
  <a class="dest-card" style="left:367px;top:1775px;background:linear-gradient(180deg,#5d7aa0,#d6a25e 45%,#2a2a2e)" role="img" aria-label="Foto: Strand mit Palmen bei Sonnenuntergang"><span class="shade"></span><span class="country">Spanien</span><span class="region">Andalusien</span></a>
  <a class="dest-card" style="left:610px;top:1775px;background:linear-gradient(180deg,#d9dcdf,#a9aca8 45%,#4e5a3e)" role="img" aria-label="Foto: Weinberge und Dorf über einem See"><span class="shade"></span><span class="country">Schweiz</span><span class="region">Genfer See</span></a>
  <a class="dest-card" style="left:853px;top:1775px;background:linear-gradient(180deg,#c58562,#b26f4f 50%,#4f3a30)" role="img" aria-label="Foto: historisches Gebäude mit Fensterläden"><span class="shade"></span><span class="country">Frankreich</span><span class="region">Gironde/Aquitanien</span></a>
</section>

<section class="why">
  <h2 class="section-title">WARUM CAMPING?</h2>
  <div class="why-col" style="left:205px">
    <h3>Camping liegt voll im Trend</h3>
    <p>Der Spaß beim Camping hängt entscheidend davon ab, ob die Camper die richtigen Campingplätze aussuchen. Somit kommt beim Camping der Suche nach einem passenden Campingplatz für Camping eine enorm hohe Bedeutung zu. Camping hat in den letzten Jahren immer mehr Freunde gefunden. Nicht zuletzt, da sich die Qualität von Campingplätzen in Deutschland aber auch z.B. Italien, Frankreich, Kroatien, Schweiz oder Spanien enorm verbessert hat. Dies liegt unter anderem auch an den verbesserten Camping Einrichtungen der Campingplaetze.</p>
  </div>
  <div class="why-col" style="left:610px">
    <p>Letztlich liegt der Trend zum Camping aber vor allem daran, das keine andere Art zu Reisen eine derart naturnahe, flexibel und erholsam ist wir Camping auf einem schönen Campingplatz in jedem Land. Campingplaetze ziehen Urlauber magisch an. Während man bei anderen Urlaubsarten lange vorher eine Reise buchen muss, sich an genaue Abflug- und Ankunftszeiten halten muss und auf einen einzigen Urlaubsort beschränkt ist, erlaubt Camping auf einem oder mehreren der unzähligen Campingplätze die Möglichkeit, seinen Urlaub flexibel zu gestalten. Man muss für schönes Camping eben nur den schönsten Zeltplatz aussuchen. Aber welches sind die schönsten Campingplaetze ?</p>
  </div>
</section>

<footer class="site-footer">
  <p>© Zeltwiese 2017 | Campingplatz anmelden | Impressum | Kontakt</p>
  <h4>Länderauswahl</h4>
  <p class="country-links">Campingplätze Deutschland | Campingplätze Belgien | Campingplätze Dänemark |Campingplätze England |Campingplätze Frankreich | Campingplätze Italien | Campingplätze Niederlande | Campingplätze Schweiz |Campingplätze Spanien | Campingplätze Österreich</p>
</footer>

</div>
</body>
</html>
```